Website redesign

Looking to redesign our existing website. (quill7meadows.com.au)
New design needs to be bright, fun and have an easy flowing.
The website needs to be design with call to action.

Some examples of other websites:
fernquaylo.com
tovanmilk.com.au

We are happy with the content of our existing website.

Target Market(s)

other businesses

Industry/Entity Type

Business Service

Number of Pages Required

5+ page

Requirements
Must have
• Theme redesign
Cool animation similar to fernquaylo.com

```html
<!DOCTYPE html>
<html lang="en">
<head>
<meta charset="utf-8">
<title>Quill 7 Meadows — Virtual Assistants</title>
<link href="https://fonts.googleapis.com/css2?family=Rubik:wght@400;500;700&family=Roboto:wght@400;500;700&display=swap" rel="stylesheet">
<style>
:root{
  --navy:#0f2236;
  --navy-btn:#0c1c2c;
  --blue:#1497c9;
  --blue-bright:#19a6dc;
  --blue-deep:#0b4a6e;
  --ink:#1b2430;
  --muted:#6b7785;
  --mist:#f3f6f9;
  --line:#dfe5ea;
  --white:#fff;
}
*{box-sizing:border-box;margin:0;padding:0}
html,body{width:1200px;height:4231px;overflow:hidden;background:var(--white)}
body{font-family:"Roboto",Arial,sans-serif;color:var(--ink);position:relative}
.abs{position:absolute}
h1,h2,h3{font-family:"Rubik",Arial,sans-serif}

/* header */
.site-header{position:absolute;left:0;top:0;width:1200px;height:75px;background:var(--white);z-index:3}
.brand{position:absolute;left:108px;top:18px;display:flex;align-items:center;gap:8px;font-family:"Rubik",sans-serif;font-weight:500;font-size:15px;color:var(--navy)}
.brand-dot{width:18px;height:18px;border-radius:50%;background:var(--blue)}
.main-nav{position:absolute;left:410px;top:29px;display:flex;gap:28px;font-size:14px;color:var(--ink)}
.main-nav span.caret::after{content:"";display:inline-block;margin-left:4px;border:4px solid transparent;border-top:5px solid var(--ink);vertical-align:-1px}
.login{position:absolute;left:885px;top:29px;font-size:14px;font-weight:500}
.signup{position:absolute;left:956px;top:22px;width:135px;height:31px;background:var(--navy-btn);color:#fff;font-size:13px;font-weight:700;display:flex;align-items:center;justify-content:center}

/* hero */
.hero-copy{left:108px;top:228px;color:#fff;width:440px}
.hero-copy h1{font-size:32px;font-weight:700;line-height:40px}
.hero-copy p{font-size:12.5px;line-height:21px;margin-top:12px;opacity:.9}
.hero-input{left:108px;top:404px;width:279px;height:36px;background:#fff;border:2px solid #d9e4ea;font-size:11px;color:#9aa5ae;padding:10px 12px}
.hero-btn{left:108px;top:451px;width:279px;height:35px;background:var(--blue-bright);color:#fff;font-size:14px;font-weight:700;display:flex;align-items:center;justify-content:center}
.hero-art{left:560px;top:213px;width:576px;height:362px;border-radius:10px;background:linear-gradient(135deg,#5bc5ec,#2a93c4 60%,#d6dde2)}

/* intro */
.video{left:108px;top:771px;width:513px;height:339px;border:9px solid #d6dce0;border-radius:10px;background:linear-gradient(120deg,#3f6f8a,#1f3c52 55%,#2f4c62)}
.intro{left:690px;top:800px;width:400px}
.intro h2{font-size:30px;font-weight:500;line-height:36px;color:var(--ink)}
.intro p{font-size:11px;line-height:20px;color:var(--muted);margin-top:24px}
.btn-blue{background:var(--blue);color:#fff;font-weight:700;display:flex;align-items:center;justify-content:center;box-shadow:0 0 0 3px #d7e7ef}
.intro-btn{left:690px;top:1034px;width:136px;height:41px;font-size:14px}

/* why */
.why{left:108px;top:1312px;width:440px}
.why h2{font-size:29px;font-weight:500}
.why p{font-size:11.5px;line-height:20px;color:var(--muted);margin-top:12px}
.feature{width:200px}
.feature h3{display:flex;align-items:center;gap:10px;font-size:16px;font-weight:500;color:var(--ink);text-transform:uppercase}
.feature .ico{width:37px;height:37px;border-radius:50%;background:var(--blue-bright);display:flex;align-items:center;justify-content:center}
.feature p{font-size:10px;line-height:14px;color:var(--muted);margin-top:12px}
.stats{left:611px;top:1313px;width:479px;height:360px;background:var(--mist)}
.stat{position:absolute;width:190px;text-align:center}
.stat b{display:block;font-family:"Rubik",sans-serif;font-size:29px;font-weight:500;color:var(--blue)}
.stat span{font-size:14px;color:var(--muted)}

/* services */
.services-title{left:0;top:1966px;width:1200px;text-align:center;color:#fff;font-size:30px;font-weight:500}
.service{position:absolute;width:491px;height:262px;display:flex;align-items:flex-end;justify-content:center;padding-bottom:22px;color:#fff;font-family:"Rubik",sans-serif;font-size:22px;font-weight:500}

/* faq */
.faq-intro{left:108px;top:2808px;width:420px}
.faq-intro h2{font-size:30px;font-weight:500;line-height:39px}
.faq-intro p{font-size:11.5px;line-height:20px;color:var(--muted);margin-top:18px}
.faq-btn{left:108px;top:3001px;width:166px;height:41px;font-size:11px;background:linear-gradient(90deg,#0f8fc2,#0b4a6e)}
.faq{left:639px;top:2778px;width:451px}
.faq-item{border-bottom:1px solid var(--line);padding:0 0 18px;margin-bottom:22px}
.faq-item h3{display:flex;justify-content:space-between;font-size:18px;font-weight:500;color:var(--ink)}
.faq-item.open h3{color:var(--blue-bright)}
.faq-item p{font-size:10px;line-height:16px;color:var(--muted);margin-top:10px}

/* quote */
.quote{left:108px;top:3181px;width:982px;height:618px;background:linear-gradient(135deg,#1a8dc0,#0e7bb0 60%,#0d6d9e);box-shadow:0 0 0 8px #e4e9ed}
.quote h2{position:absolute;left:0;top:103px;width:982px;text-align:center;color:#fff;font-size:29px;font-weight:500}
.field{position:absolute;background:rgba(255,255,255,.28);border:1px solid rgba(255,255,255,.35);color:#dbeef7;font-size:11px;padding:12px 14px}
.check{position:absolute;left:53px;top:442px;display:flex;align-items:center;gap:7px;color:#fff;font-size:11px}
.check i{width:11px;height:11px;border:1px solid #fff}
.submit{position:absolute;left:53px;top:472px;width:136px;height:41px;background:var(--navy-btn);border:2px solid #2b4a64;color:#fff;font-size:12px;font-weight:700;display:flex;align-items:center;justify-content:center}
.perks{position:absolute;left:503px;top:176px;width:427px;height:337px;background:#fff;padding:34px 38px}
.perks h3{font-size:19px;font-weight:500;letter-spacing:.5px}
.perks small{display:block;font-size:10px;color:var(--muted);margin-top:4px}
.perks ul{list-style:none;margin-top:30px}
.perks li{display:flex;align-items:center;gap:8px;font-size:11px;color:#3a4652;height:30px}
.perks li i{width:12px;height:12px;border-radius:50%;background:var(--blue-bright);position:relative}
.perks li i::after{content:"";position:absolute;left:3px;top:2px;width:4px;height:6px;border:solid #fff;border-width:0 1.5px 1.5px 0;transform:rotate(45deg)}

/* footer */
.site-footer{left:0;top:3694px;width:1200px;height:537px;background:var(--navy);color:#fff}
.foot-col{position:absolute;top:208px}
.foot-col h4{font-family:"Rubik",sans-serif;font-size:18px;font-weight:500;letter-spacing:.5px}
.foot-col ul{list-style:none;margin-top:25px}
.foot-col li{font-size:12px;height:26px;color:#d8e0e7}
.foot-rule{position:absolute;left:108px;top:471px;width:982px;height:1px;background:#25384b}
.copyright{position:absolute;left:108px;top:496px;font-size:10.5px;color:#c9d3dc}
.social{position:absolute;top:486px;width:30px;height:30px;border-radius:50%;background:#fff}
</style>
</head>
<body>

<svg class="abs" style="left:0;top:0" width="1200" height="3694" viewBox="0 0 1200 3694">
  <defs>
    <linearGradient id="heroGrad" x1="0" y1="0" x2="1" y2="0.4">
      <stop offset="0" stop-color="#0b4a6e"/><stop offset="1" stop-color="#1290c4"/>
    </linearGradient>
    <linearGradient id="servGrad" x1="0" y1="0" x2="1" y2="1">
      <stop offset="0" stop-color="#1590c6"/><stop offset="1" stop-color="#0b4a6e"/>
    </linearGradient>
  </defs>
  <polygon points="0,600 1200,560 1200,1140 919,1207 0,1130" fill="var(--mist)"/>
  <polygon points="0,673 1200,585 1200,640 0,690" fill="#d7e6f1"/>
  <polygon points="0,75 1200,75 1200,583 0,673" fill="url(#heroGrad)"/>
  <polygon points="0,1778 919,1872 1200,1778 1200,2676 0,2676" fill="url(#servGrad)"/>
  <polyline points="0,1790 919,1884 1200,1790" fill="none" stroke="#cfe4f0" stroke-width="4"/>
  <polygon points="0,1770 919,1864 1200,1770 1200,1760 0,1760" fill="#fff"/>
</svg>

<header class="site-header">
  <div class="brand"><span class="brand-dot"></span>QUILL 7 MEADOWS</div>
  <nav class="main-nav">
    <span class="caret">Company</span><span class="caret">Solutions</span><span class="caret">Blog</span><span>Contact</span>
  </nav>
  <div class="login">LOG IN</div>
  <div class="signup">SIGN UP</div>
</header>

<section class="hero">
  <div class="abs hero-copy">
    <h1>Virtual Assistant?<br>More Like Valuable Asset!</h1>
    <p>Lorem ipsum dolor sit amet, consectetur adipiscing elit sed do eiusmod tempor incididunt ut labore et dolore magna</p>
  </div>
  <div class="abs hero-input">Email</div>
  <div class="abs hero-btn">Let's get started</div>
  <div class="abs hero-art" role="img" aria-label="Illustration of a desktop monitor and laptop showing a robot assistant at work"></div>
</section>

<section class="intro-section">
  <div class="abs video" role="img" aria-label="Video still of two team members introducing the service"></div>
  <div class="abs intro">
    <h2>Outsourcing. A big word that means big things for your business.</h2>
    <p>Virtual Assistants are the superheroes of the modern office. They can do everything your team can do on a computer at a fraction of the price! (Well, maybe not high five you when you've had a win, but a virtual high five is definitely on the table!)</p>
  </div>
  <div class="abs btn-blue intro-btn">Learn more</div>
</section>

<section class="why-section">
  <div class="abs why">
    <h2>Why We Are</h2>
    <p>Lorem ipsum dolor sit amet, consectetur adipiscing elit, sed do eiusmod tempor incididunt ut labore et dolore magna aliqua quis ipsum suspendisse</p>
  </div>
  <div class="abs feature" style="left:108px;top:1437px"><h3><span class="ico"><svg width="16" height="16" viewBox="0 0 16 16"><path d="M3 13 L6 8 L11 3 L13 3 L13 5 L8 10 Z" fill="#fff"/></svg></span>Fast services</h3><p>Lorem ipsum dolor sit amet, consectetur adipiscing elit, sed do eiusmod tempor incidi ut labore et</p></div>
  <div class="abs feature" style="left:363px;top:1437px"><h3><span class="ico"><svg width="16" height="16" viewBox="0 0 16 16"><circle cx="8" cy="4" r="2" fill="#fff"/><circle cx="3.5" cy="12" r="2" fill="#fff"/><circle cx="12.5" cy="12" r="2" fill="#fff"/></svg></span>Team work</h3><p>Lorem ipsum dolor sit amet, consectetur adipiscing elit, sed do eiusmod tempor incidi ut labore et</p></div>
  <div class="abs feature" style="left:108px;top:1574px"><h3><span class="ico"><svg width="16" height="16" viewBox="0 0 16 16"><circle cx="8" cy="8" r="5" fill="none" stroke="#fff" stroke-width="2"/><circle cx="8" cy="8" r="2" fill="#fff"/></svg></span>Transparency</h3><p>Lorem ipsum dolor sit amet, consectetur adipiscing elit, sed do eiusmod tempor incidi ut labore et</p></div>
  <div class="abs feature" style="left:363px;top:1574px"><h3><span class="ico"><svg width="16" height="16" viewBox="0 0 16 16"><path d="M3 3 L13 13 M13 3 L3 13" stroke="#fff" stroke-width="2"/></svg></span>24/7 Support</h3><p>Lorem ipsum dolor sit amet, consectetur adipiscing elit, sed do eiusmod tempor incidi ut labore et</p></div>

  <div class="abs stats">
    <svg class="abs" style="left:0;top:0" width="479" height="360"><line x1="240" y1="30" x2="240" y2="330" stroke="#d3dbe2"/><line x1="50" y1="180" x2="430" y2="180" stroke="#d3dbe2"/></svg>
    <div class="stat" style="left:52px;top:78px"><b>2651</b><span>Happy Client</span></div>
    <div class="stat" style="left:240px;top:78px"><b>820</b><span>Total Staff</span></div>
    <div class="stat" style="left:52px;top:226px"><b>130</b><span>International Award</span></div>
    <div class="stat" style="left:246px;top:226px"><b>1233</b><span>Complete Projects</span></div>
  </div>
</section>

<section class="services-section">
  <h2 class="abs services-title">Our Services</h2>
  <div class="service" style="left:108px;top:2044px;background:linear-gradient(180deg,#2d5f8c,#1b3f66)" role="img" aria-label="Photo of a recruiter with a headset">We recruit Virtual Assistants</div>
  <div class="service" style="left:599px;top:2044px;background:linear-gradient(180deg,#5b6670,#2b3540)" role="img" aria-label="Photo of a laptop beside network cabling">Tech support</div>
  <div class="service" style="left:108px;top:2306px;background:linear-gradient(180deg,#3b6a92,#1d3c5c)" role="img" aria-label="Photo of hands configuring a phone system">Set up the phone system</div>
  <div class="service" style="left:599px;top:2306px;background:linear-gradient(180deg,#4a7ca3,#25517a)" role="img" aria-label="Photo of a support agent with a headset">We manage Virtual Assistants</div>
</section>

<section class="faq-section">
  <div class="abs faq-intro">
    <h2>Have Question About Your Our Services?</h2>
    <p>Lorem ipsum dolor sit amet, consectetur adipisicing elit, sed do eiusmod tempor incididunt ut labore et dolore magna aliqua. Ut enim ad minim veniam dolor</p>
  </div>
  <div class="abs btn-blue faq-btn">ASK YOUR QUESTION</div>
  <div class="abs faq">
    <div class="faq-item"><h3>Risus commodo viverra maecenas accumsan <span>+</span></h3></div>
    <div class="faq-item"><h3>Risus commodo viverra maecenas <span>+</span></h3></div>
    <div class="faq-item open"><h3>Risus commodo viverra <span>-</span></h3><p>Lorem ipsum dolor sit amet, consectetur adipiscing elit, sed do eiusmod tempor incididunt ut labore et dolore magna aliqua. Quis ipsum suspendisse ultrices gravida. Risus commodo viverra maecenas accumsan lacus vel facilisis.</p></div>
    <div class="faq-item"><h3>Risus commodo viverra maecenas accumsan <span>+</span></h3></div>
  </div>
</section>

<footer class="abs site-footer">
  <div class="foot-col" style="left:108px"><h4>RESOURCES</h4><ul><li>Features</li><li>History</li><li>Blog</li><li>Help</li><li>Policy</li></ul></div>
  <div class="foot-col" style="left:530px"><h4>FOLLOW US</h4><ul><li>Codeharbor</li><li>Chirpline</li><li>Shotboard</li><li>Friendwall</li><li>Snapgrid</li></ul></div>
  <div class="foot-col" style="left:949px"><h4>MORE</h4><ul><li>Contact</li><li>FAQs</li><li>Test Suite APi</li><li>About</li><li>Terms</li></ul></div>
  <div class="foot-rule"></div>
  <div class="copyright">Copyright © 2020 quill7meadows. All Rights Reserved.</div>
  <span class="social" style="left:975px"></span>
  <span class="social" style="left:1018px"></span>
  <span class="social" style="left:1060px"></span>
</footer>

<section class="abs quote">
  <h2>Get A Quote</h2>
  <div class="field" style="left:53px;top:176px;width:206px;height:40px">First Name</div>
  <div class="field" style="left:274px;top:176px;width:206px;height:40px">Last Name</div>
  <div class="field" style="left:53px;top:232px;width:206px;height:40px">Phone</div>
  <div class="field" style="left:274px;top:232px;width:206px;height:40px">Email</div>
  <div class="field" style="left:53px;top:288px;width:427px;height:134px">Message...</div>
  <div class="check"><i></i>Subscribe to our newsletter</div>
  <div class="submit">SUBMIT</div>
  <div class="perks">
    <h3>IT'S QUILL 7 MEADOWS</h3>
    <small>Why are we your new best outsourcing friend?</small>
    <ul>
      <li><i></i>Your Own Virtual Assistant</li>
      <li><i></i>One Invoice Per Month</li>
      <li><i></i>No Super or TAX</li>
      <li><i></i>Dedicated To Your Business Only</li>
      <li><i></i>Dedicated Phone System</li>
      <li><i></i>IT Setup and Support</li>
    </ul>
  </div>
</section>

</body>
</html>
```